New Website for Asia Travel Agency

Lanternpath Journeys Website

We want a redesign for our current website, www.lanternpathjourneys.example. We want you to get creative with our brand and present our company in a unique, creative and compelling way, that communicates our exotic destinations and tours, the local and authentic character of our travel consultants and the trustworthy and professional nature of our company.

Who is this company?

Lanternpath Journeys is an online tour operator specializing in providing tailor-made tours to eight destinations in Asia; Vietnam, Thailand, Laos, Cambodia, Indonesia, Myanmar, Japan and China. They were launched in mid February 2012 with headquarters in Bangkok, Thailand, and staffed by locals and expats with many years of experience in the travel industry, and who are committed to sharing their deep knowledge of, and passion for the region.

Local knowledge

Our consultants at Lanternpath Journeys are all locals – they know their destinations inside-out and draw upon invaluable first-hand experience and information when planning your tour. They have insights into local culture and tradition, they know the best places to visit, the most worthwhile experiences to have and, most importantly, they have the knowledge to create exactly the holiday you desire.

All hotels and activities featured in a Lanternpath Journeys tour are regularly inspected by our consultants to ensure the highest quality standards are met and that all information is correct and up to date.

Unforgettable Travel Experiences

Whether it's a cultural exploration or a beach holiday you're after – or a mix of both – Lanternpath Journeys has an itinerary for you – and if we don't have one, we'll tailor-make one! From the main sights to remote villages, our locally based Travel Specialists will give you unique insights into every place you visit and let you delve into known destinations from new perspectives.

Our tours offer a variety of hotel and resort options, premium stays in deluxe accommodation, heritage hotels, a five-star boutique or on the water in a junk. Tap into our experience let us create an experience unique to you – and one you will never forget.

What type of Holiday to Asia?

Our itineraries at Lanternpath Journeys are created according to different inspirations. Some travelers are interested in the History & Culture of a destination, while some like to stay active with Adventure tours. A Cross Border trip explores different countries in a single tour, while Velvet Summit tours offer the highest level of exclusivity across our destinations. There are 14 different Holiday Types to choose from, or you can mix and match ideas to create your dream vacation.

Target Market(s)

Slightly more female, aged 30-65, are creative, professional and looking for something different, something a bit unusual.

Industry/Entity Type

Boutique

Requirements
Must have
• 5 page designs:

1. Homepage
2. Tours list page for a country
3. Tour page
4. 'Be Inspired' page
5. Country page
6. Enquiry page

Our inspirations.

The following list shows websites we love and which inspire us... to give you some indication of our preferred styles, functions and layouts:

http://www.frostmeridian.example/en/ (we really like this, great personality, like the use of icons for tour types)
http://www.pebblewalks.example.uk/ (very simple design elements and layout)
http://www.sunvalecoast.example/ (great use of background image, nice simple nav bar)
http://www.roamcedarfall.example/ (we like because it has distinct personality and is well suited to the destination)
http://www.seemarlowton.example/ (clear personality through font use)
http://www.vastroving.example/ (original, unique)
http://www.wanderquill.example/long-loop-of-asia (like the map style)

Key design points:

1. You must use our existing logo (attached), but you can change the color scheme of the logo to accord with the whichever color scheme you choose for the main designs.
2. Our logo strapline is "Asia is our Lanternpath" and should be used prominently on the page to reinforce the meaning of our company name.
3. Home page and tours list pages should allow the user to see the choice of tours immediately without scrolling & Introduction copy should be minimal.
4. We and our site visitors are inspired and excited by our photography, this is an element of the site which we would like to maintain and build on, though the section page header sliders are currently too big and do not allow quick access to the section content. This is a design problem which needs a solution. Full page photographic backgrounds may be an answer?
5. Tour page should display other contextual tours, from the same country or style/type
6. We should promote press coverage in various places
7. We should display consultant profiles in various places
8. Map designs for tour page and country page, plus a modal pop out for the home page. These are complex and may have a few small photos and short descriptive text only, though this is limited by your own creativity. We will use graphics and html5/css3 so there are no creative limitations.
9. The 'Inspirations' / 'Be Inspired' page is for people who want travel and holiday ideas, who are looking for inspiration on where to go and what to do. This section needs to reflect the exotic, the unusual, the extraordinary in our destinations and tours, and we leave this to your creative genius to develop. We are also interested in how this inspirations page is related to the blog and social media content we produce daily, is there an integration here? Can we present YouTube videos, our blog posts, Facebook posts etc, on this page? This is another design challenge.
10. We would like to see designs for the tours list page which feature AJAX content filtering (for instance: http://demo.layoutbrisk.example/?acn), we would like to see how to include this type of content filtering on homepage and destination page also.
11. The 'Enquiry' call to action should be on all pages and prominent.
12. The enquiry page can reflect the same fields as the existing website enquiry page

Values to be communicated:

- Exotic: Asia is exotic, and our tours will expose clients to extraordinary sights and unusual cultural encounters.
- Authentic: Our travel consultants all live in the destinations themselves, they are local nationals and have all the insider knowledge to give clients a truly authentic experience of our destinations
- Unique: All of our tours are tailor made, there are no fixed departure dates or join-in groups. All tour itineraries can be uniquely designed for our clients, from departure dates to destinations.
- Trust: Some travelers prefer to book their holidays with local agencies they can meet in person, rather than with online companies like us who live in the destinations and who they only get to meet on Skype video or phone. We want to convey that we are trustworthy. We have attempted this through presenting a 'meet the team' page and a 'press' page and advert, as well as offering a prominent international phone number. How we you build on this and further convey this value?

```html
<!DOCTYPE html>
<html lang="en">
<head>
<meta charset="utf-8">
<title>Lanternpath Journeys</title>
<link href="https://fonts.googleapis.com/css2?family=Jost:wght@400;500&display=swap" rel="stylesheet">
<style>
:root{
  --orange:#f7941d;
  --red:#c4161c;
  --yellow:#f2c500;
  --blue:#2b8fd1;
  --green:#8cc63f;
  --grey-nav:#b5b5b5;
  --ink:#2b2b2b;
  --body:#555;
  --beige:#e8e0dc;
  --beige-dark:#ded4cf;
  --charcoal:#4a4a4a;
  --charcoal-deep:#333;
  --panel:#f7f7f7;
  --white:#fff;
}
*{box-sizing:border-box;margin:0;padding:0}
html,body{width:746px;height:1200px;overflow:hidden}
body{position:relative;font-family:"Jost",Arial,sans-serif;color:var(--body);background:var(--white);font-size:8px}
.abs{position:absolute}
.photo{position:absolute}

/* hero */
.hero{left:0;top:0;width:746px;height:280px;background:linear-gradient(180deg,#7a6a4a 0%,#d9a94e 35%,#f0c46a 55%,#a7865a 80%,#6a5a40 100%)}
.site-header{left:97px;top:0;width:553px;height:58px;display:flex}
.brand{width:204px;height:58px;background:rgba(255,255,255,.92);display:flex;align-items:center;padding-left:14px;gap:8px}
.brand-mark{width:22px;height:22px;background:var(--charcoal)}
.brand-name{font-size:13px;color:var(--charcoal);line-height:1.1}
.brand-name small{display:block;font-size:6.5px}
.main-nav{display:flex}
.nav-item{width:58px;height:58px;background:rgba(200,200,200,.85);border-top:4px solid var(--grey-nav);color:var(--white);font-size:6.5px;text-transform:uppercase;display:flex;flex-direction:column;align-items:center;justify-content:flex-end;padding-bottom:5px;gap:6px}
.nav-item.home{background:var(--red);border-top-color:var(--red)}
.nav-item.c1{border-top-color:var(--yellow)}
.nav-item.c2{border-top-color:var(--orange)}
.nav-item.c3{border-top-color:var(--blue)}
.nav-item.c4{border-top-color:var(--green)}
.nav-item svg{width:16px;height:16px}

.search-panel{left:513px;top:78px;width:121px;height:160px;background:rgba(255,255,255,.85);padding:8px 10px;font-size:5.5px;color:#666}
.search-tabs{display:flex;border-bottom:2px solid var(--orange);margin-bottom:8px}
.search-tabs span{padding:4px 6px;font-size:6px}
.search-tabs .on{background:var(--orange);color:var(--white)}
.field-label{text-transform:uppercase;margin-bottom:2px}
.select{height:11px;border:1px solid #ccc;background:var(--white);margin-bottom:8px;padding-left:4px;line-height:10px;color:#aaa;position:relative}
.select::after{content:"";position:absolute;right:0;top:0;width:10px;height:9px;background:#ddd}
.search-btn{margin:4px auto 0;width:56px;height:13px;background:var(--orange);color:var(--white);text-align:center;line-height:13px;font-size:6px}

.hero-title{left:120px;top:224px;font-size:18px;color:var(--white);letter-spacing:.3px}
.hero-cta{left:112px;top:250px;width:80px;height:15px;background:var(--orange);color:var(--white);font-size:9px;line-height:15px;padding-left:10px}
.pager{left:478px;top:250px;display:flex;gap:3px}
.pager span{width:15px;height:14px;background:rgba(255,255,255,.3);color:var(--ink);font-size:7px;text-align:center;line-height:14px}
.pager .on{background:var(--orange);color:var(--white)}

/* country strip */
.country-band{left:0;top:280px;width:746px;height:150px;background:linear-gradient(180deg,#cfc3a8,#b9ac90 60%,#a89c82)}
.country-card{position:absolute;background:var(--white);box-shadow:0 2px 5px rgba(0,0,0,.35)}
.country-card .thumb{width:100%}
.country-card .label{height:24px;background:linear-gradient(#e0e0e0,#bcbcbc);color:var(--ink);text-align:center;line-height:24px;font-size:10px;text-transform:uppercase}
.strip-arrow{width:14px;height:20px;background:rgba(255,255,255,.5);display:flex;align-items:center;justify-content:center}
.strip-arrow.next{background:var(--orange)}

/* intro */
.intro-title{left:110px;top:442px;font-size:17px;color:var(--ink);width:382px;border-bottom:1px solid #ccc;padding-bottom:6px}
.intro-copy{left:110px;top:479px;width:380px;font-size:7px;line-height:1.45;color:#666}
.intro-copy p{margin-bottom:9px}
.enquiry-box{left:513px;top:430px;width:124px;height:168px;background:var(--beige)}
.enquiry-head{text-align:center;font-size:9.5px;color:var(--ink);padding-top:15px;line-height:1.25}
.phone-band{margin-top:8px;height:35px;background:var(--orange);color:var(--white);text-align:center;padding-top:4px;font-size:12.5px}
.phone-band small{display:block;font-size:6px}
.testimonial{padding:10px 8px 0 26px;position:relative;font-size:6.5px;color:#555;line-height:1.3}
.testimonial::before{content:"\201C";position:absolute;left:6px;top:2px;font-size:26px;color:#bbb}
.testimonial h4{font-weight:400;font-size:8px;color:var(--ink);margin-bottom:4px}

/* tabs */
.tab{top:598px;height:28px;font-size:7.5px;text-transform:uppercase;display:flex;align-items:center;gap:6px;padding-left:9px;color:var(--white);background:var(--charcoal)}
.tab.on{background:var(--beige);color:var(--ink)}
.tab svg{width:11px;height:11px}

/* destinations */
.dest-band{left:0;top:625px;width:746px;height:155px;background:var(--beige)}
.dest-card{position:absolute;top:645px;width:119px;height:113px;background:var(--white)}
.dest-card .thumb{height:77px}
.dest-card .cap{text-align:center;font-size:6.5px;color:var(--ink);padding-top:9px;text-transform:uppercase}
.dest-card .tools{display:flex;justify-content:center;gap:8px;margin-top:3px}
.dest-card svg{width:9px;height:9px}
.chev{font-size:22px;color:var(--ink);line-height:1}

/* promotions */
.promo-panel{left:97px;top:780px;width:553px;height:196px;background:var(--panel);box-shadow:0 0 6px rgba(0,0,0,.15)}
.promo-title{left:110px;top:795px;font-size:14px;color:var(--ink)}
.promo-count{left:594px;top:797px;font-size:9px;color:var(--ink)}
.promo-count b{color:var(--orange);font-weight:500}
.promo-card{position:absolute;top:828px;width:148px}
.promo-card .thumb{margin:0 3px;height:70px}
.promo-card .meta{margin:0 3px;height:22px;background:#b8b8b8;color:var(--white);font-size:6px;padding:3px 0 0 12px;position:relative}
.promo-card .meta span{display:block;color:#eee;font-size:5.5px}
.promo-card .zoom{position:absolute;right:2px;top:2px;width:18px;height:18px;background:#555}
.promo-card.hot .zoom{background:var(--orange)}
.promo-card .actions{height:32px;background:var(--charcoal);color:var(--white);font-size:6.5px;display:flex;align-items:center;justify-content:space-around;padding:0 6px;text-transform:uppercase}
.promo-card.hot .actions{background:var(--orange)}
.promo-card .actions span{display:flex;align-items:center;gap:4px}
.seal{left:107px;top:825px;width:36px;height:36px;border-radius:50%;background:var(--charcoal-deep)}

/* footer */
.footer{left:0;top:976px;width:746px;height:224px;background:var(--charcoal)}
.footer-ground{left:0;top:1100px;width:746px;height:100px;background:linear-gradient(180deg,rgba(60,60,60,0),#3d3d3d 60%,#2f3a3c)}
.social-bar{left:97px;top:993px;width:553px;height:27px;background:#e9e9e9;display:flex;align-items:center;font-size:7px;color:var(--ink)}
.social-bar .follow{width:175px;padding-left:14px;display:flex;align-items:center;gap:5px;height:100%;background:#dcdcdc}
.social-bar .sq{width:12px;height:12px;background:#8a8a8a}
.social-bar .tweet{padding-left:170px}
.social-bar .tweet b{font-weight:500;margin-right:6px}
.foot-col{top:1046px;font-size:7px;color:#eee;line-height:1.58}
.foot-col h5{font-weight:400;color:var(--orange);font-size:8px;text-transform:uppercase;margin-bottom:1px}
.newsletter{left:440px;top:1042px;width:196px;text-align:right;font-size:7px;color:#eee;line-height:1.4}
.newsletter h5{font-weight:400;color:var(--orange);font-size:8px;text-transform:uppercase}
.subscribe{left:559px;top:1086px;width:78px;height:19px;background:var(--orange);color:var(--white);text-align:center;line-height:19px;font-size:9px;text-transform:uppercase}
</style>
</head>
<body>

<div class="abs photo hero" role="img" aria-label="Ancient stone temple columns against a golden sunset sky"></div>

<header class="abs site-header">
  <div class="brand">
    <span class="brand-mark"></span>
    <span class="brand-name">Lanternpath Journeys<small>Asia is our Lanternpath.</small></span>
  </div>
  <nav class="main-nav">
    <div class="nav-item home"><svg viewBox="0 0 16 16" fill="none" stroke="#fff" stroke-width="1.5"><path d="M2 8 8 2l6 6M4 7v7h8V7"/></svg>Home</div>
    <div class="nav-item c1"><svg viewBox="0 0 16 16" fill="#444"><path d="M7 1h2l1 6 5 3v2l-5-1-1 3 2 1v1H5v-1l2-1-1-3-5 1v-2l5-3z"/></svg>Destinations</div>
    <div class="nav-item c2"><svg viewBox="0 0 16 16" fill="none" stroke="#444" stroke-width="1.4"><path d="M8 15V1M3 3h9l2 2-2 2H3z"/></svg>Tour</div>
    <div class="nav-item c3"><svg viewBox="0 0 16 16" fill="none" stroke="#444" stroke-width="1.4"><circle cx="4" cy="10" r="3"/><circle cx="12" cy="10" r="3"/><path d="M7 10h2M1 9 3 4M15 9l-2-5"/></svg>Be inspired</div>
    <div class="nav-item c4"><svg viewBox="0 0 16 16" fill="none" stroke="#444" stroke-width="1.3"><circle cx="8" cy="8" r="6.5"/><ellipse cx="8" cy="8" rx="3" ry="6.5"/><path d="M1.5 8h13"/></svg>Country</div>
    <div class="nav-item"><svg viewBox="0 0 16 16" fill="#444"><path d="M1 6c2-4 12-4 14 0l-3 1-1-2H5L4 7zM4 8h8l2 6H2z"/></svg>Enquiry</div>
  </nav>
</header>

<form class="abs search-panel">
  <div class="search-tabs"><span class="on">✈ TOURS</span><span>HOTELS</span></div>
  <div class="field-label">Select a country:</div>
  <div class="select">ALL COUNTRIES</div>
  <div class="field-label">Select a city:</div>
  <div class="select">ALL CITIES</div>
  <div class="field-label">Duration:</div>
  <div class="select">ALL DURATIONS</div>
  <div class="search-btn">SEARCH</div>
</form>

<h1 class="abs hero-title" style="font-weight:400">THE BEST OF MYANMAR</h1>
<div class="abs hero-cta">find out more</div>
<div class="abs pager"><span>1</span><span>2</span><span>3</span><span class="on">4</span><span>5</span><span>6</span><span>7</span><span>8</span><span>9</span></div>

<section class="abs photo country-band" role="img" aria-label="Weathered temple ruins in soft daylight"></section>
<div class="abs strip-arrow" style="left:106px;top:344px"><svg width="6" height="10" viewBox="0 0 6 10"><path d="M5 1 1 5l4 4" stroke="#fff" stroke-width="1.5" fill="none"/></svg></div>
<div class="abs strip-arrow next" style="left:621px;top:344px"><svg width="6" height="10" viewBox="0 0 6 10"><path d="M1 1l4 4-4 4" stroke="#fff" stroke-width="1.5" fill="none"/></svg></div>

<div class="country-card" style="left:113px;top:303px;width:87px"><div class="thumb" role="img" aria-label="Harbour at dusk" style="height:78px;background:linear-gradient(#8fb4d8,#3d6a8c)"></div><div class="label">Indonesia</div></div>
<div class="country-card" style="left:200px;top:297px;width:110px"><div class="thumb" role="img" aria-label="Autumn tree" style="height:91px;background:linear-gradient(#d86a1c,#a34a10 70%,#5a3a1a)"></div><div class="label">Thailand</div></div>
<div class="country-card" style="left:440px;top:297px;width:102px"><div class="thumb" role="img" aria-label="Tree at sunset" style="height:91px;background:linear-gradient(#8a2a08,#e8902a 60%,#3a1a08)"></div><div class="label">Japan</div></div>
<div class="country-card" style="left:542px;top:303px;width:84px"><div class="thumb" role="img" aria-label="Stone tower on a green hill" style="height:78px;background:linear-gradient(#6a9ac8,#9ab870 70%,#5a7a3a)"></div><div class="label">China</div></div>
<div class="country-card" style="left:310px;top:290px;width:130px;z-index:2"><div class="thumb" role="img" aria-label="Rock pinnacles under a full moon" style="height:97px;background:linear-gradient(#0d1a4a,#24408a 50%,#d9a43a)"></div><div class="label" style="height:33px;line-height:33px;font-size:11px">Australia</div></div>

<h2 class="abs intro-title" style="font-weight:400">ASIA IS OUR LANTERNPATH</h2>
<div class="abs intro-copy">
  <p>No one knows a destination better than someone who lives, works and plays there. That's the foundation of Lanternpath Journeys. Our travel specialists reside in Asia. They live Asia, they breathe Asia. And they're intrigued explorers as much as they are citizens of Bangkok, or Bali, or Luang Prabang.</p>
  <p>The result is a travel company tailor-made for the person with a taste for veering off the well-trodden path, for the adventurer who wants access to Asia's most spectacular sights, but hidden charms as well, on the road less traveled.</p>
  <p>Want to explore this Asia? Step into our Lanternpath.</p>
</div>

<aside class="abs enquiry-box">
  <div class="enquiry-head">CLICK HERE TO<br>Send an Enqiry<br>or call toll free:</div>
  <div class="phone-band">+800-4417-3061<small>+(INTERNATIONAL DIAL CODE)</small></div>
  <div class="testimonial"><h4>A JAVANESE JOURNEY</h4>We had a great trip. Thank you so much for all the preparation work to get the itinerary just right.</div>
</aside>

<div class="abs tab on" style="left:110px;width:100px"><svg viewBox="0 0 12 12"><path d="M6 11 2.5 5.5A3.5 3.5 0 1 1 9.5 5.5z" fill="#333"/></svg>Hot destinations</div>
<div class="abs tab" style="left:211px;width:100px"><svg viewBox="0 0 12 12" fill="none" stroke="#fff"><path d="M3 1v8h8M1 3h8v8"/></svg>New creations</div>
<div class="abs tab" style="left:313px;width:99px"><svg viewBox="0 0 12 12" fill="none" stroke="#fff"><rect x="1" y="2" width="10" height="8"/><circle cx="6" cy="6" r="2"/></svg>Last viewed</div>

<section class="abs dest-band"></section>
<div class="abs chev" style="left:95px;top:672px">‹</div>
<div class="abs chev" style="left:639px;top:670px">›</div>

<div class="dest-card" style="left:119px"><div class="thumb" role="img" aria-label="Old wooden house under a cloudy sky" style="background:linear-gradient(#4a6a8a,#6a5a4a 60%,#3a3a2a)"></div><div class="cap">The best of Myanmar</div><div class="tools"><svg viewBox="0 0 9 9" fill="none" stroke="#333"><circle cx="3.5" cy="3.5" r="2.5"/><path d="M5.5 5.5 8.5 8.5"/></svg><svg viewBox="0 0 9 9" fill="#333"><rect x="0" y="2" width="9" height="6"/></svg></div></div>
<div class="dest-card" style="left:248px"><div class="thumb" role="img" aria-label="Boat on a calm lake at sunset" style="background:linear-gradient(#e8b88a,#c88a5a 60%,#6a5a3a)"></div><div class="cap">Saung beach retreat</div><div class="tools"><svg viewBox="0 0 9 9" fill="none" stroke="#333"><circle cx="3.5" cy="3.5" r="2.5"/><path d="M5.5 5.5 8.5 8.5"/></svg><svg viewBox="0 0 9 9" fill="#333"><rect x="0" y="2" width="9" height="6"/></svg></div></div>
<div class="dest-card" style="left:377px"><div class="thumb" role="img" aria-label="Jetty over turquoise water" style="background:linear-gradient(#2a6ab8,#3ac0c8 60%,#1a8a8a)"></div><div class="cap">Saung beach retreat</div><div class="tools"><svg viewBox="0 0 9 9" fill="none" stroke="#333"><circle cx="3.5" cy="3.5" r="2.5"/><path d="M5.5 5.5 8.5 8.5"/></svg><svg viewBox="0 0 9 9" fill="#333"><rect x="0" y="2" width="9" height="6"/></svg></div></div>
<div class="dest-card" style="left:505px"><div class="thumb" role="img" aria-label="Rocky shore under a dramatic sky" style="background:linear-gradient(#2a4a9a,#e8a04a 55%,#2a3a5a)"></div><div class="cap">Saung beach retreat</div><div class="tools"><svg viewBox="0 0 9 9" fill="none" stroke="#333"><circle cx="3.5" cy="3.5" r="2.5"/><path d="M5.5 5.5 8.5 8.5"/></svg><svg viewBox="0 0 9 9" fill="#333"><rect x="0" y="2" width="9" height="6"/></svg></div></div>

<section class="abs promo-panel"></section>
<h2 class="abs promo-title" style="font-weight:400">OUR FEATURED PROMOTIONS</h2>
<div class="abs promo-count"><b>‹ 1</b> to 7 ›</div>

<div class="promo-card hot" style="left:127px"><div class="thumb" role="img" aria-label="Pier at dusk with blue sky" style="background:linear-gradient(#1a3a8a,#4a7ac8 60%,#3a4a5a)"></div><div class="meta">A JAVANESE JOURNEY<span>$1153 (15% Off)</span><i class="zoom"></i></div><div class="actions"><span>✈ View tour</span><span>▤ Send an inquiry</span></div></div>
<div class="promo-card" style="left:297px"><div class="thumb" role="img" aria-label="Boat in reeds under a bright sun" style="background:linear-gradient(#6a9ad8,#e8d08a 45%,#4a6a3a)"></div><div class="meta">A JAVANESE JOURNEY<span>$1153 (15% Off)</span><i class="zoom"></i></div><div class="actions"><span>✈ View tour</span><span>▤ Send an inquiry</span></div></div>
<div class="promo-card" style="left:468px"><div class="thumb" role="img" aria-label="Ancient amphitheatre with fireworks at night" style="background:linear-gradient(#0a1a4a,#2a3a7a 50%,#b88a4a)"></div><div class="meta">A JAVANESE JOURNEY<span>$1153 (15% Off)</span><i class="zoom"></i></div><div class="actions"><span>✈ View tour</span><span>▤ Send an inquiry</span></div></div>
<div class="abs seal" role="img" aria-label="Hot deal badge"></div>

<footer class="abs footer"></footer>
<div class="abs photo footer-ground" role="img" aria-label="Faint city skyline silhouette"></div>

<div class="abs social-bar">
  <div class="follow"><b style="font-weight:500;margin-right:8px">FOLLOW US ON:</b><i class="sq"></i><i class="sq"></i><i class="sq"></i><i class="sq"></i><i class="sq"></i></div>
  <div class="tweet" style="padding-left:73px"><b>LATEST TWEET</b>“If you're considering bringing your kids on #holiday to #Asia, here ...”</div>
</div>

<div class="abs foot-col" style="left:120px"><h5>Quick links</h5>Home<br>Destinations<br>Tours<br>Holiday Types<br>Best Value<br>About Us<br>Blog</div>
<div class="abs foot-col" style="left:215px"><h5>Our Lanternpath</h5>Thailand<br>Indonesia<br>Laos<br>Cambodia<br>Japan<br>Myanmar<br>Vietnam<br>China<br>Multi-Country</div>
<div class="abs foot-col" style="left:309px"><h5>About Lanternpath Journeys</h5>Why Book With Us<br>About Us<br>Meet The Team<br>Careers<br>In The Press<br>Affiliate Program</div>
<div class="abs newsletter"><h5>✉ Subscribe to our e-newsletter</h5>Sign up for Lanternpath Journeys' e-newsletter<br>featuring promotions, travel musings and insider destination</div>
<div class="abs subscribe">Subscribe</div>

</body>
</html>
```